Business Card & Stationery Design for a General Contracting Company
Brenwick Contracting Limited
Tolvane Perdo
Managing Director
No 7 Marlowe Crescent, Elmsby
brenwickcontracting@quillpost.net
The Company is involved in supply and transport of aggregate materials and heavy equipment rental at present. Furthermore we recently had a project for the logo design of our Company on this website and we would like to incorporate this logo into our stationery designs and business cards. Please see the links below; Our design project; http://orders.markcraftstudio.net/contests/logo-for-a-general-contracting-company The logo chosen; http://orders.markcraftstudio.net/drafts/display/contest/512093/draft/e7d4b58213690ab1c5f93d478ee2bb718204617

```html
<!DOCTYPE html>
<html lang="en">
<head>
<meta charset="utf-8">
<title>Brenwick Contracting Limited – Business Card</title>
<link rel="stylesheet" href="https://fonts.googleapis.com/css2?family=Roboto+Condensed:ital,wght@0,400;0,700;1,400;1,700&display=swap">
<style>
  :root {
    --page-bg: #dcdcdc;
    --card-white: #ffffff;
    --brand-blue: #1f5ba2;
    --brand-navy: #1a3a6c;
    --brand-red: #cf3030;
    --line-white: rgba(255,255,255,0.85);
    --text-white: #ffffff;
    --faint-white: rgba(255,255,255,0.12);
  }
  * { margin: 0; padding: 0; box-sizing: border-box; }
  html, body { width: 1200px; height: 842px; overflow: hidden; }
  body {
    background: var(--page-bg);
    font-family: "Roboto Condensed", sans-serif;
    position: relative;
  }
  .card {
    position: absolute;
    top: 272px;
    width: 520px;
    height: 297px;
    overflow: hidden;
    box-shadow: 0 6px 18px rgba(0,0,0,0.18);
  }
  .card-front { left: 50px; background: var(--card-white); }
  .card-back { left: 630px; background: var(--brand-blue); }

  /* Front */
  .front-brand {
    position: absolute;
    left: 28px; top: 44px;
    display: flex; align-items: center; gap: 12px;
  }
  .brand-dot {
    width: 34px; height: 34px; border-radius: 50%;
    background: var(--brand-red);
  }
  .brand-name {
    font-weight: 700;
    font-size: 21px;
    letter-spacing: 0.5px;
    text-transform: uppercase;
    color: var(--brand-navy);
    line-height: 1;
  }
  .front-panel {
    position: absolute;
    left: 0; top: 120px; width: 520px; height: 177px;
    background: var(--brand-blue);
  }
  .divider-vertical {
    position: absolute; left: 250px; top: 0; width: 1px; height: 177px;
    background: var(--line-white);
  }
  .divider-horizontal {
    position: absolute; left: 250px; top: 92px; width: 270px; height: 1px;
    background: var(--line-white);
  }
  .contact-block {
    position: absolute; left: 22px; top: 14px; width: 220px;
    color: var(--text-white);
  }
  .contact-address { font-size: 12px; margin-bottom: 22px; }
  .contact-line { font-size: 9.5px; line-height: 15px; }
  .person {
    position: absolute; left: 268px; top: 108px;
    color: var(--text-white);
  }
  .person-name { font-style: italic; font-weight: 700; font-size: 15px; }
  .person-title { font-style: italic; font-size: 11px; margin-top: 2px; }

  /* Back */
  .back-mark {
    position: absolute; left: 130px; top: 30px;
  }
  .back-web {
    position: absolute; right: 24px; bottom: 22px;
    color: var(--text-white);
    font-size: 13px; letter-spacing: 2px;
  }
</style>
</head>
<body>
  <section class="card card-front">
    <div class="front-brand">
      <span class="brand-dot"></span>
      <span class="brand-name">Brenwick Contracting Limited</span>
    </div>
    <div class="front-panel">
      <div class="divider-vertical"></div>
      <div class="divider-horizontal"></div>
      <div class="contact-block">
        <p class="contact-address">No 7 Marlowe Crescent, Elmsby</p>
        <p class="contact-line">Tel: 555 0142</p>
        <p class="contact-line">Cell: 555 0163</p>
        <p class="contact-line">Fax: 555 0187</p>
        <p class="contact-line">brenwickcontracting@quillpost.net</p>
        <p class="contact-line">www.brenwickcontracting.net</p>
      </div>
      <div class="person">
        <p class="person-name">Tolvane Perdo</p>
        <p class="person-title">Managing Director</p>
      </div>
    </div>
  </section>

  <section class="card card-back">
    <svg class="back-mark" width="260" height="220" viewBox="0 0 260 220" role="img" aria-label="Faint company name decoration">
      <circle cx="130" cy="110" r="100" fill="none" stroke="var(--faint-white)" stroke-width="10"/>
      <text x="130" y="116" text-anchor="middle" font-family="Roboto Condensed, sans-serif" font-weight="700" font-size="17" fill="var(--faint-white)">BRENWICK CONTRACTING LIMITED</text>
    </svg>
    <p class="back-web">www.brenwickcontracting.net</p>
  </section>
</body>
</html>
```